Wedding Photo Studio needs custom webpage

I'm changing up my service offering to offer multiple editing styles. I'm looking to update my website to reflect that but still showcase my dreamy edits as an attention grabbing part of the website.

I will have 4 color editing styles (Lucian's Hallmark, Bright & Airy, Velvet Umber, Dreamy) and one black and white style. I have attached sample images in each style.

I also attached a couple dreamy edits that can be used as attention grabbing images.

I'm hoping for some functionality that perhaps takes a single image and divides it by 4 to show 25% in each style that can be clicked on and would 'maximize' the carousel to that style but still have a functionality to go to a different style after being maximized.

You can see www.lucianvphotography-demo.com for the current design and content. It doesn't have to be too different (but can be). It just needs to showcase the multiple editing styles effectively.

Target Market(s)

Couples who are having $20-50k weddings.

Industry/Entity Type

Photography

Coding

Coded - Design and coding required

Number of Pages Required

3 page

Colors

Designer to choose colors to be used in the design.

Requirements
Must have
• Pricing page with toggles for (off-season/on-season, Saturday/non-saturday) accurate pricing, good way to show multiple editing style photos.

```html
<!DOCTYPE html>
<html lang="en">
<head>
<meta charset="utf-8">
<title>LucianV Photography – Kitchener-Waterloo Wedding Photographer</title>
<link rel="stylesheet" href="https://fonts.googleapis.com/css2?family=Mulish:wght@400;500;600&family=Playfair+Display:ital,wght@0,400;1,400&display=swap">
<style>
:root{
  --blue:#1f5fa8;
  --blue-deep:#0f5aa6;
  --ink:#3a3a3a;
  --text:#555;
  --pale:#dde8f2;
  --white:#fff;
  --dark:#1c1c1c;
  --star:#f2c14e;
  --card-border:#e3e3e3;
}
*{box-sizing:border-box;margin:0;padding:0}
html,body{width:1200px;height:3429px;overflow:hidden;background:var(--white)}
body{font-family:"Mulish",sans-serif;color:var(--text)}
.page{position:relative;width:1200px;height:3429px;overflow:hidden}
.abs{position:absolute}
.serif{font-family:"Playfair Display",serif;font-style:italic;font-weight:400}
.serif .accent{color:var(--blue)}

/* header */
.brand{left:0;width:1200px;top:26px;text-align:center;font-size:27px;color:var(--blue);letter-spacing:1px}
.brand small{display:block;font-family:"Mulish",sans-serif;font-style:normal;font-size:10px;letter-spacing:2px;color:var(--ink);margin-top:2px}
.search{left:1012px;top:44px}
.nav{top:110px;font-size:13px;color:var(--ink);letter-spacing:.3px;text-transform:uppercase;transform:translateX(-50%);white-space:nowrap}
.nav.active{color:var(--blue)}

/* hero */
.hero{left:31px;top:142px;width:1138px;height:429px;background:linear-gradient(180deg,#3f8fd6 0%,#5aa6e0 35%,#3a4a66 60%,#1b2235 100%)}
.hero-card{left:53px;top:306px;width:290px;height:245px;background:var(--blue-deep);color:var(--white);text-align:center}
.hero-kicker{top:32px;width:100%;font-size:13px;font-weight:600;letter-spacing:.5px}
.hero-title{top:64px;width:100%;font-size:28px;line-height:40px}
.btn-light{left:61px;top:171px;width:168px;height:38px;border:1px solid var(--white);font-size:13px;font-weight:600;line-height:36px;letter-spacing:.3px}

/* section headings: text followed by a short rule */
.heading-row{display:flex;align-items:center;gap:20px;white-space:nowrap}
.heading-row.centered{left:0;width:1200px;justify-content:center}
.heading{font-size:30px;line-height:44px;color:#555}
.rule{display:block;flex:0 0 65px;height:1px;background:var(--blue);margin-top:6px}
.about-text{left:193px;top:716px;width:814px;text-align:center;font-size:15px;line-height:34.4px;color:#555}

/* styles */
.pale-block{left:663px;top:958px;width:537px;height:392px;background:var(--pale)}
.photo{overflow:hidden}
.vline{width:1px;background:var(--blue)}
.style-label{font-size:24px;color:#333;text-align:center;transform:translateX(-50%);white-space:nowrap}
.style-label.selected{color:var(--blue)}
.btn-outline{border:1px solid var(--blue);color:var(--blue);font-size:14px;font-weight:500;text-align:center;letter-spacing:.3px}

/* testimonials */
.testimonial-band{left:0;top:1852px;width:1200px;height:367px;background:linear-gradient(180deg,#e7c9b9 0%,#efd8c8 35%,#dfe1d8 60%,#c9cf9a 100%)}
.card{width:316px;height:435px;top:2107px;background:var(--white);border:1px solid var(--card-border);text-align:center}
.stars{top:36px;left:0;width:100%;display:flex;justify-content:center;gap:5px}
.quote{top:74px;left:30px;width:256px;font-size:15px;line-height:34.2px;color:#555}
.avatar{left:46px;top:336px;width:66px;height:66px;border-radius:50%}
.couple{left:140px;top:358px;font-size:15px;font-weight:600;color:var(--blue);letter-spacing:.5px;white-space:nowrap}

/* footer */
.footer{left:0;top:3043px;width:1200px;height:386px;background:var(--dark)}
.split{top:2794px;height:355px}
.footer-brand{left:0;width:1200px;top:3196px;text-align:center;color:var(--white);font-size:34px;letter-spacing:1px}
.footer-brand small{display:block;font-family:"Mulish",sans-serif;font-style:normal;font-size:13px;letter-spacing:2px;margin-top:2px}
.footer-nav{left:0;width:1200px;top:3324px;text-align:center;color:var(--white);font-size:13px;font-weight:600;letter-spacing:.3px}
.footer-nav span{margin:0 14px}
.copyright{left:0;width:1200px;top:3372px;text-align:center;color:var(--white);font-size:12px;font-weight:600;letter-spacing:.5px}
</style>
</head>
<body>
<main class="page">

  <!-- header -->
  <div class="abs brand serif">LucianV<small>PHOTOGRAPHY</small></div>
  <svg class="abs search" width="16" height="16" viewBox="0 0 16 16" aria-label="Search"><circle cx="6.5" cy="6.5" r="4.8" fill="none" stroke="#333" stroke-width="1.5"/><line x1="10" y1="10" x2="14" y2="14" stroke="#333" stroke-width="1.5"/></svg>
  <nav>
    <span class="abs nav active" style="left:291px">Home</span>
    <span class="abs nav" style="left:403px">The Team</span>
    <span class="abs nav" style="left:534px">Portfolio</span>
    <span class="abs nav" style="left:648px">Blog</span>
    <span class="abs nav" style="left:749px">Pricing</span>
    <span class="abs nav" style="left:882px">Contact Me</span>
  </nav>

  <!-- hero -->
  <div class="abs hero" role="img" aria-label="Wedding ceremony in a glass-walled hall with guests seated at gold tables"></div>
  <div class="abs hero-card">
    <div class="abs hero-kicker">LUCIANV PHOTOGRAPHY</div>
    <div class="abs hero-title serif">Kitchener-Waterloo<br>Wedding Photographer</div>
    <div class="abs btn-light">GET STARTED NOW</div>
  </div>

  <!-- about -->
  <div class="abs heading-row centered" style="top:646px">
    <h2 class="heading serif">About <span class="accent">LucianV Photography</span></h2>
    <span class="rule"></span>
  </div>
  <p class="abs about-text">I am an accountant by day, photographer by night. I once read a happy life is had by loving your job, loving your creative hobby and the love of family; photography is one part of that for me. I focus primarily on wedding photography in southern Ontario. I cover Toronto, Hamilton, Kitchener, Waterloo, London and anywhere in the world you want to send me. If you like what I do, please reach out; I'm happy to meet with you and chat more about your big day.</p>

  <!-- editing styles -->
  <div class="abs pale-block"></div>
  <div class="abs heading-row centered" style="top:946px">
    <h2 class="heading serif">Our <span class="accent">Editing Styles</span></h2>
    <span class="rule"></span>
  </div>

  <div class="abs photo" style="left:106px;top:1024px;width:278px;height:374px;background:linear-gradient(160deg,#8a8076 0%,#a3523f 45%,#7a6d62 70%,#c9c2ba 100%)" role="img" aria-label="Couple on stone steps beside autumn foliage, Lucian's Hallmark edit"></div>
  <div class="abs photo" style="left:408px;top:1075px;width:382px;height:504px;background:linear-gradient(160deg,#b7ada3 0%,#d78b7c 45%,#a59a8d 70%,#e6e1dc 100%)" role="img" aria-label="Couple on stone steps beside autumn foliage, Bright and Airy edit"></div>
  <div class="abs photo" style="left:815px;top:1024px;width:279px;height:374px;background:linear-gradient(160deg,#6e3a2c 0%,#8c4a35 40%,#3b2b26 65%,#d9cfc7 100%)" role="img" aria-label="Groom kissing bride's forehead in front of autumn leaves, Velvet Umber edit"></div>

  <div class="abs vline" style="left:245px;top:1421px;height:48px"></div>
  <div class="abs style-label serif selected" style="left:245px;top:1482px">Lucian's Hallmark</div>
  <svg class="abs" style="left:282px;top:1512px" width="20" height="22" viewBox="0 0 20 22" aria-hidden="true"><path d="M6 2v11l-2-2c-1-1-2.5 0-1.6 1.2L7 19c1 1.5 2 2 4 2h3c2.5 0 4-1.8 4-4.5V11c0-1-1.5-1.2-1.8 0V9.5c0-1-1.600-1.2-1.8 0V8.8c0-1-1.7-1.1-1.8 0V2c0-1.4-2-1.4-2 0z" fill="#fff" stroke="#222" stroke-width="1"/></svg>
  <div class="abs vline" style="left:955px;top:1421px;height:48px"></div>
  <div class="abs style-label serif" style="left:955px;top:1482px">Velvet Umber</div>
  <div class="abs vline" style="left:600px;top:1603px;height:47px"></div>
  <div class="abs style-label serif" style="left:600px;top:1661px">Bright &amp; Airy</div>
  <div class="abs btn-outline" style="left:515px;top:1727px;width:170px;height:38px;line-height:36px">VIEW OUR STYLES</div>

  <!-- testimonials -->
  <div class="abs testimonial-band" role="img" aria-label="Dreamy edit of a couple embracing on a snowy golf course at sunset"></div>
  <div class="abs heading-row" style="left:743px;top:1920px">
    <h2 class="heading serif">Our <span class="accent">Testimonials</span></h2>
    <span class="rule"></span>
  </div>

  <article class="abs card" style="left:110px">
    <div class="abs stars"><svg width="16" height="16" viewBox="0 0 24 24"><path d="M12 2l3 7 7 .6-5.4 4.7 1.7 7.2L12 17.8 5.7 21.5l1.7-7.2L2 9.6 9 9z" fill="var(--star)"/></svg><svg width="16" height="16" viewBox="0 0 24 24"><path d="M12 2l3 7 7 .6-5.4 4.7 1.7 7.2L12 17.8 5.7 21.5l1.7-7.2L2 9.6 9 9z" fill="var(--star)"/></svg><svg width="16" height="16" viewBox="0 0 24 24"><path d="M12 2l3 7 7 .6-5.4 4.7 1.7 7.2L12 17.8 5.7 21.5l1.7-7.2L2 9.6 9 9z" fill="var(--star)"/></svg><svg width="16" height="16" viewBox="0 0 24 24"><path d="M12 2l3 7 7 .6-5.4 4.7 1.7 7.2L12 17.8 5.7 21.5l1.7-7.2L2 9.6 9 9z" fill="var(--star)"/></svg><svg width="16" height="16" viewBox="0 0 24 24"><path d="M12 2l3 7 7 .6-5.4 4.7 1.7 7.2L12 17.8 5.7 21.5l1.7-7.2L2 9.6 9 9z" fill="var(--star)"/></svg></div>
    <p class="abs quote">Lucian is the absolute best! He did a SPECTACULAR job with our wedding photos. He got images of everything, even the things that we never thought he would notice. Hands down Lucian is the best photographer...</p>
    <div class="abs avatar" style="background:linear-gradient(135deg,#c98a8a,#6d5a78)" role="img" aria-label="Couple portrait"></div>
    <div class="abs couple">RORY &amp; AMARA</div>
  </article>

  <article class="abs card" style="left:442px">
    <div class="abs stars"><svg width="16" height="16" viewBox="0 0 24 24"><path d="M12 2l3 7 7 .6-5.4 4.7 1.7 7.2L12 17.8 5.7 21.5l1.7-7.2L2 9.6 9 9z" fill="var(--star)"/></svg><svg width="16" height="16" viewBox="0 0 24 24"><path d="M12 2l3 7 7 .6-5.4 4.7 1.7 7.2L12 17.8 5.7 21.5l1.7-7.2L2 9.6 9 9z" fill="var(--star)"/></svg><svg width="16" height="16" viewBox="0 0 24 24"><path d="M12 2l3 7 7 .6-5.4 4.7 1.7 7.2L12 17.8 5.7 21.5l1.7-7.2L2 9.6 9 9z" fill="var(--star)"/></svg><svg width="16" height="16" viewBox="0 0 24 24"><path d="M12 2l3 7 7 .6-5.4 4.7 1.7 7.2L12 17.8 5.7 21.5l1.7-7.2L2 9.6 9 9z" fill="var(--star)"/></svg><svg width="16" height="16" viewBox="0 0 24 24"><path d="M12 2l3 7 7 .6-5.4 4.7 1.7 7.2L12 17.8 5.7 21.5l1.7-7.2L2 9.6 9 9z" fill="var(--star)"/></svg></div>
    <p class="abs quote">We got married September 30 and hired Lucian and we are VERY HAPPY we did! Lucian did an AMAZING job!! He is very professional, very organized, got the most beautiful shots, he captured...</p>
    <div class="abs avatar" style="background:linear-gradient(135deg,#9a9a9a,#2e2e2e)" role="img" aria-label="Black and white couple portrait"></div>
    <div class="abs couple">BEN &amp; CARLA</div>
  </article>

  <article class="abs card" style="left:773px">
    <div class="abs stars"><svg width="16" height="16" viewBox="0 0 24 24"><path d="M12 2l3 7 7 .6-5.4 4.7 1.7 7.2L12 17.8 5.7 21.5l1.7-7.2L2 9.6 9 9z" fill="var(--star)"/></svg><svg width="16" height="16" viewBox="0 0 24 24"><path d="M12 2l3 7 7 .6-5.4 4.7 1.7 7.2L12 17.8 5.7 21.5l1.7-7.2L2 9.6 9 9z" fill="var(--star)"/></svg><svg width="16" height="16" viewBox="0 0 24 24"><path d="M12 2l3 7 7 .6-5.4 4.7 1.7 7.2L12 17.8 5.7 21.5l1.7-7.2L2 9.6 9 9z" fill="var(--star)"/></svg><svg width="16" height="16" viewBox="0 0 24 24"><path d="M12 2l3 7 7 .6-5.4 4.7 1.7 7.2L12 17.8 5.7 21.5l1.7-7.2L2 9.6 9 9z" fill="var(--star)"/></svg><svg width="16" height="16" viewBox="0 0 24 24"><path d="M12 2l3 7 7 .6-5.4 4.7 1.7 7.2L12 17.8 5.7 21.5l1.7-7.2L2 9.6 9 9z" fill="var(--star)"/></svg></div>
    <p class="abs quote">Lucian did an outstanding job on our wedding photos! We got so so much more for so so much less. Thanks again Lucian, you exceeded our expectations and then some. I recommend him 100 times over...</p>
    <div class="abs avatar" style="background:linear-gradient(135deg,#dfe6ee,#5a6f8e)" role="img" aria-label="Couple portrait by the water"></div>
    <div class="abs couple">THEO &amp; NINA</div>
  </article>

  <div class="abs btn-outline" style="left:486px;top:2586px;width:228px;height:38px;line-height:36px">VIEW MORE TESTIMONIALS</div>

  <!-- style explorer -->
  <div class="abs heading-row centered" style="top:2696px">
    <h2 class="heading serif">Seamlessly Explore: <span class="accent">Click, Maximize, and Switch Between Styles!</span></h2>
    <span class="rule"></span>
  </div>

  <div class="abs footer"></div>
  <div class="abs split" style="left:112px;width:244px;background:linear-gradient(160deg,#6e7480,#4a4f58 60%,#7e7060)" role="img" aria-label="Groom holding bride's hand by a waterfall, style one"></div>
  <div class="abs split" style="left:356px;width:244px;background:linear-gradient(160deg,#8a96a3,#3c4656 55%,#9c8f7f)" role="img" aria-label="Groom by a waterfall, style two"></div>
  <div class="abs split" style="left:600px;width:243px;background:linear-gradient(160deg,#8a6e55,#c9b8a6 55%,#7b5b42)" role="img" aria-label="Bride in lace gown, style three"></div>
  <div class="abs split" style="left:843px;width:245px;background:linear-gradient(160deg,#5f7a4a,#3f5a34 50%,#8a5a3a)" role="img" aria-label="Evergreen trees beside the couple, style four"></div>

  <!-- footer -->
  <div class="abs footer-brand serif">LucianV<small>PHOTOGRAPHY</small></div>
  <div class="abs footer-nav"><span>HOME</span>|<span>THE TEAM</span>|<span>PORTFOLIO</span>|<span>BLOG</span>|<span>PRICING</span>|<span>CONTACT ME</span></div>
  <div class="abs copyright">COPYRIGHT 2025 LUCIAN VARGA PHOTOGRAPHY.</div>

</main>
</body>
</html>
```